Re-design a highly converting profile page for my website

My website allows people to book a mentor for long-term mentorship as well as sessions. I would like to re-design this site within our branding guidelines to give people the best profile possible.

Please give this website a modern look and concentrate on the CTA and conversion rates. This is a highly converting site and it should stay that way or even get better!

Please also keep menu bar & footer in tact

Target Market(s)

Developers, Designers, Entrepreneurs in the Tech industry

Number of Pages Required

1 page

Requirements
Must have
• Strong CTA, existing color palette, testimonials and major elements
Nice to have
• Modern look, easy to see CTA, easy to scan offer. Not too crowded
Should not have
• No reporpusing. It is and stays a profile page

```html
<!DOCTYPE html>
<html lang="en">
<head>
<meta charset="utf-8">
<title>Evan Carter – 1-on-1 Product Mentorship</title>
<link href="https://fonts.googleapis.com/css2?family=Raleway:wght@400;500;600;700;800&family=Poppins:wght@400;500;600;700&family=Roboto:ital,wght@0,300;0,400;0,500;1,400&display=swap" rel="stylesheet">
<style>
:root{
  --navy:#2f3e5c;
  --navy-deep:#2b3a66;
  --ink:#2a2a2a;
  --text:#444;
  --blue:#1a9ee8;
  --blue-dark:#0b88cf;
  --blue-bright:#2196f3;
  --card-border:#eceff3;
  --white:#fff;
}
*{box-sizing:border-box;margin:0;padding:0}
html,body{width:1200px;height:3038px;overflow:hidden}
body{position:relative;background:var(--white);font-family:"Roboto",sans-serif;color:var(--text)}
.abs{position:absolute}

/* nav */
.site-nav{position:absolute;left:0;top:0;width:1200px;height:83px;background:var(--navy)}
.brand-dot{position:absolute;left:100px;top:14px;width:55px;height:55px;border-radius:50%;background:var(--white)}
.nav-link{position:absolute;top:28px;font-family:"Raleway",sans-serif;font-size:19px;font-weight:500;color:var(--white)}
.nav-star{position:absolute;left:920px;top:29px}
.login-btn{position:absolute;left:974px;top:21px;width:125px;height:41px;border:2px solid var(--white);border-radius:3px;color:var(--white);font-family:"Raleway",sans-serif;font-size:19px;font-weight:500;text-align:center;line-height:37px}

/* hero */
.hero-title{position:absolute;left:98px;top:236px;font-family:"Raleway",sans-serif;font-weight:800;font-size:46px;color:var(--ink);letter-spacing:-.3px}
.hero-title .accent{color:var(--navy-deep)}
.hero-sub{position:absolute;left:98px;top:300px;font-family:"Raleway",sans-serif;font-size:31px;font-weight:500;color:#2d2d2d}
.btn-dark{position:absolute;height:46px;background:var(--navy);color:var(--white);font-family:"Open Sans","Raleway",sans-serif;font-weight:600;font-size:20px;text-align:center;line-height:46px;border-radius:2px}
.hero-art{position:absolute;left:518px;top:120px}

/* about */
.about-photo{position:absolute;left:100px;top:658px;width:378px;height:355px;background:linear-gradient(160deg,#d9d9d9,#8a8a8a 60%,#5d5d5d)}
.about-band{position:absolute;left:100px;top:903px;width:509px;height:110px;background:var(--navy)}
.about-word{position:absolute;left:420px;top:660px;width:80px;height:350px;overflow:hidden}
.about-word span{position:absolute;left:72px;top:0;transform-origin:0 0;transform:rotate(90deg) translateY(-4px);white-space:nowrap;font-family:"Poppins",sans-serif;font-weight:700;font-size:62px;color:var(--navy);line-height:1}
.about-heading{position:absolute;left:667px;top:668px;font-family:"Poppins",sans-serif;font-weight:700;font-size:27px;line-height:41px;color:var(--navy-deep)}
.about-copy{position:absolute;left:667px;width:432px;font-size:11.2px;line-height:18.4px;color:#444}
.about-copy b{color:var(--navy-deep);font-weight:500}
.btn-blue{position:absolute;background:var(--blue);color:var(--white);font-family:"Open Sans","Poppins",sans-serif;font-weight:500;text-align:center;border-radius:2px}

/* section headings */
.section-title{position:absolute;left:0;width:1200px;text-align:center;font-family:"Poppins",sans-serif;font-weight:700;font-size:33px;color:var(--navy-deep)}
.section-rule{position:absolute;height:4px;background:var(--navy-deep)}

/* pricing */
.price-card{position:absolute;background:var(--white);border:1px solid var(--card-border);border-radius:18px;box-shadow:0 4px 14px rgba(40,60,90,.10);overflow:hidden}
.plan-name{position:absolute;left:0;width:100%;text-align:center;font-family:"Open Sans","Roboto",sans-serif;font-weight:500;font-size:21px;color:var(--blue)}
.plan-price{position:absolute;font-family:"Raleway",sans-serif;font-weight:300;font-size:50px;color:var(--blue);line-height:1}
.plan-unit{position:absolute;font-size:7px;color:var(--blue)}
.plan-feature{position:absolute;left:0;width:100%;text-align:center;font-family:"Poppins",sans-serif;font-size:10.5px;color:#333}
.plan-feature::before{content:"";display:inline-block;width:9px;height:9px;border:1px solid #bbb;border-radius:50%;margin-right:9px;vertical-align:-1px}
.plan-rule{position:absolute;height:1px;background:#e6e6e6}
.ribbon{position:absolute;right:-28px;top:14px;width:110px;height:17px;background:var(--blue-bright);transform:rotate(45deg);color:var(--white);font-size:7px;text-align:center;line-height:17px}

.wave{position:absolute;left:0;top:1580px}

/* features */
.feature-card{position:absolute;top:1825px;width:229px;height:312px;background:var(--white);border-radius:16px;box-shadow:0 3px 14px rgba(40,60,90,.12)}
.feature-card svg{position:absolute;left:57px;top:40px}
.feature-label{position:absolute;left:0;top:193px;width:100%;text-align:center;font-family:"Raleway",sans-serif;font-weight:500;font-size:27px;color:var(--navy)}

/* testimonial */
.quote-card{position:absolute;left:329px;top:2345px;width:542px;height:339px;border:1px solid #d8d8d8;border-radius:18px;box-shadow:0 2px 8px rgba(0,0,0,.06)}
.quote-badge{position:absolute;left:526px;top:2290px}
.quote-text{position:absolute;left:345px;top:2467px;width:510px;text-align:center;font-style:italic;font-size:11.3px;line-height:18.4px;color:#444}
.quote-name{position:absolute;left:0;top:2582px;width:1200px;text-align:center;font-family:"Poppins",sans-serif;font-weight:600;font-size:22px;color:#333}
.carousel-arrow{position:absolute;top:2494px;width:42px;height:42px;border-radius:50%;background:var(--white);box-shadow:0 2px 8px rgba(0,0,0,.15)}
.carousel-arrow::after{content:"";position:absolute;left:10px;top:10px;width:22px;height:22px;border-radius:50%;background:var(--blue-bright)}
.carousel-arrow svg{position:absolute;left:15px;top:15px;z-index:1}

/* footer */
.site-footer{position:absolute;left:0;top:2768px;width:1200px;height:270px;background:var(--navy);border-top:7px solid var(--blue-bright)}
.footer-dot{position:absolute;left:100px;top:28px;width:84px;height:84px;border-radius:50%;background:var(--white)}
.footer-brand{position:absolute;left:98px;top:126px;font-family:"Raleway",sans-serif;font-weight:700;font-size:26px;color:var(--white)}
.footer-tag{position:absolute;left:99px;top:164px;width:300px;font-size:15px;line-height:23px;color:var(--white)}
.footer-heading{position:absolute;left:568px;top:28px;font-family:"Raleway",sans-serif;font-weight:600;font-size:24px;color:var(--blue-bright)}
.footer-list{position:absolute;list-style:none;font-size:17.5px;line-height:27.5px;color:var(--white)}
.social-dot{position:absolute;top:181px;width:24px;height:24px;border-radius:50%;background:var(--white)}
.social-dot.active{background:var(--blue-bright)}
</style>
</head>
<body>

<header class="site-nav">
  <div class="brand-dot" aria-label="GuideHarbor"></div>
  <span class="nav-link" style="left:517px">Dashboard</span>
  <span class="nav-link" style="left:643px">Management</span>
  <span class="nav-link" style="left:790px">Your Profile</span>
  <svg class="nav-star" width="22" height="22" viewBox="0 0 24 24"><path fill="#fff" d="M12 2l2.9 6.6 7.1.6-5.4 4.7 1.6 7L12 17.3 5.8 21l1.6-7L2 9.2l7.1-.6z"/></svg>
  <div class="login-btn">Log In</div>
</header>

<section class="hero">
  <svg class="hero-art" width="682" height="463" viewBox="0 0 682 463">
    <path fill="#2f3e5c" d="M0 463 C70 360 120 300 260 290 C420 280 470 230 530 150 C580 90 620 80 682 100 L682 463 Z"/>
    <rect role="img" aria-label="Portrait photo of the mentor smiling" x="190" y="0" width="492" height="463" fill="url(#heroTone)" opacity=".92"/>
    <defs>
      <linearGradient id="heroTone" x1="0" y1="0" x2="0" y2="1">
        <stop offset="0" stop-color="#ffffff" stop-opacity="0"/>
        <stop offset=".15" stop-color="#d8a98c" stop-opacity=".55"/>
        <stop offset=".6" stop-color="#e08a86"/>
        <stop offset="1" stop-color="#d6787a"/>
      </linearGradient>
    </defs>
  </svg>
  <h1 class="hero-title">1-on-1 <span class="accent">Product</span> Mentorship</h1>
  <p class="hero-sub">For Your Mobile and Web products</p>
  <div class="btn-dark" style="left:99px;top:366px;width:167px">Get Free Trail</div>
  <div class="btn-dark" style="left:282px;top:366px;width:241px;top:364px">Apply For Mentorship</div>
</section>

<section class="about">
  <div class="about-band"></div>
  <div class="about-photo" role="img" aria-label="Black and white portrait photo of the mentor"></div>
  <div class="about-word"><span>About me</span></div>
  <h2 class="about-heading">Need mentor for Your Product?<br>I can help you!</h2>
  <p class="about-copy" style="top:763px">Evan Carter is passionate about creating and scaling powerful web and mobile products thatmake a significant impact in millions of people'slives around the world. Evan deeply enjoysbuilding and managing the product anddevelopment teams that help achieve that goal.</p>
  <p class="about-copy" style="top:855px">Evan is currently the <b>Director of Product at Harbor Insurance</b>. He was previously the CPO of Orbit Media which operated in the AdTech industry, helping the world's largest media companies with data-inspired storytelling. Previously a Senior Product leader at Northway Travel and Printwell Digital.</p>
  <div class="btn-blue" style="left:667px;top:947px;width:167px;height:46px;line-height:46px;font-size:20px">Book a session</div>
</section>

<section class="pricing">
  <h2 class="section-title" style="top:1088px">Pricing Table</h2>
  <div class="section-rule" style="left:537px;top:1144px;width:127px"></div>

  <article class="price-card" style="left:203px;top:1235px;width:232px;height:345px">
    <h3 class="plan-name" style="top:18px">Free Trail</h3>
    <span class="plan-price" style="left:84px;top:61px">0</span>
    <span class="plan-unit" style="left:122px;top:92px">$ /Day</span>
    <p class="plan-feature" style="top:153px">7 Days Free Trial</p>
    <div class="plan-rule" style="left:25px;top:173px;width:182px"></div>
    <p class="plan-feature" style="top:184px">Personal Mentorship</p>
    <div class="plan-rule" style="left:25px;top:204px;width:182px"></div>
    <p class="plan-feature" style="top:215px">Some Offers applied</p>
    <div class="btn-blue" style="left:36px;top:269px;width:160px;height:39px;line-height:39px;font-size:15px">Book a Session</div>
  </article>

  <article class="price-card" style="left:469px;top:1189px;width:264px;height:391px">
    <div class="ribbon">Best Deal</div>
    <h3 class="plan-name" style="top:20px;left:-6px">Personal Mentorship</h3>
    <span class="plan-price" style="left:63px;top:73px">240</span>
    <span class="plan-unit" style="left:160px;top:106px">$ /month</span>
    <p class="plan-feature" style="top:192px;left:-2px;line-height:15px">Continous and personal<br><span style="margin-left:-40px">1-1 mentorship</span></p>
    <div class="plan-rule" style="left:30px;top:228px;width:204px"></div>
    <p class="plan-feature" style="top:244px">1-on-1 Live Sessions</p>
    <div class="btn-blue" style="left:41px;top:305px;width:181px;height:44px;line-height:44px;font-size:16px;background:var(--blue-dark)">Book a Session</div>
  </article>

  <article class="price-card" style="left:766px;top:1235px;width:232px;height:345px">
    <h3 class="plan-name" style="top:18px">Coaching Session</h3>
    <span class="plan-price" style="left:51px;top:61px">150</span>
    <span class="plan-unit" style="left:138px;top:92px">$ /Session</span>
    <p class="plan-feature" style="top:153px">60 minutes</p>
    <div class="plan-rule" style="left:25px;top:173px;width:182px"></div>
    <p class="plan-feature" style="top:184px">1-0-1 Live Sessions</p>
    <div class="plan-rule" style="left:25px;top:204px;width:182px"></div>
    <p class="plan-feature" style="top:215px;left:12px">To become Product Manager</p>
    <div class="btn-blue" style="left:36px;top:269px;width:160px;height:39px;line-height:39px;font-size:15px">Book a session</div>
  </article>
</section>

<svg class="wave" width="1200" height="161" viewBox="0 0 1200 161">
  <path fill="#2f3e5c" d="M0 70 C120 90 250 85 420 50 C580 15 720 -5 880 25 C1020 52 1110 100 1200 130 L1200 161 L0 161 Z"/>
</svg>

<section class="features">
  <div class="feature-card" style="left:100px">
    <svg width="116" height="116" viewBox="0 0 116 116" fill="none" stroke="#2f3e5c" stroke-width="8" stroke-linejoin="round" stroke-linecap="round">
      <path d="M6 6h86v58H34L14 80V64H6z"/><path d="M24 24h40M24 42h56"/><path d="M92 28h18v64h-12v20L80 92H28"/>
    </svg>
    <div class="feature-label">Personal Chat</div>
  </div>
  <div class="feature-card" style="left:356px">
    <svg width="116" height="116" viewBox="0 0 116 116" fill="none" stroke="#2f3e5c" stroke-width="8" stroke-linecap="round" stroke-linejoin="round">
      <path d="M58 16a42 42 0 1 0 10 84"/><path d="M58 38a20 20 0 1 0 0 40"/><path d="M56 58L94 20M84 12l10 8-6 10"/>
      <circle cx="86" cy="86" r="26"/><path d="M74 86l9 9 16-17"/>
    </svg>
    <div class="feature-label">To-Do’s &amp; Goals</div>
  </div>
  <div class="feature-card" style="left:613px">
    <svg width="116" height="116" viewBox="0 0 116 116" fill="none" stroke="#2f3e5c" stroke-width="8" stroke-linecap="round" stroke-linejoin="round">
      <path d="M2 6h112M10 6v70h96V6"/><path d="M28 58l20-20 14 12 22-22"/><path d="M58 76v20"/><circle cx="58" cy="104" r="6"/>
    </svg>
    <div class="feature-label">Projects</div>
  </div>
  <div class="feature-card" style="left:869px">
    <svg width="116" height="116" viewBox="0 0 116 116" fill="none" stroke="#2f3e5c" stroke-width="8" stroke-linejoin="round">
      <path d="M8 6h20l10 28-14 10c10 22 26 38 48 48l10-14 28 10v22H96C48 110 6 68 6 20z"/>
    </svg>
    <div class="feature-label">1-on-1 Calls</div>
  </div>
</section>

<section class="testimonial">
  <h2 class="section-title" style="top:2188px;left:8px">Testimonial</h2>
  <div class="section-rule" style="left:553px;top:2243px;width:130px"></div>
  <div class="quote-card"></div>
  <svg class="quote-badge" width="150" height="138" viewBox="0 0 150 138">
    <path fill="#2196f3" d="M14 0h122a14 14 0 0 1 14 14v78a14 14 0 0 1-14 14H60l-38 32 4-32H14A14 14 0 0 1 0 92V14A14 14 0 0 1 14 0z"/>
    <path fill="#fff" d="M62 30c-18 4-26 16-26 32 0 12 6 20 16 20 9 0 15-6 15-14s-6-14-14-14c2-8 7-12 15-15zM104 30c-18 4-26 16-26 32 0 12 6 20 16 20 9 0 15-6 15-14s-6-14-14-14c2-8 7-12 15-15z"/>
  </svg>
  <p class="quote-text">Evan helped me set focus and intention in mygoal of scaling my independent projects.Before working with Evan I felt like I was jumping fromidea to idea with no plan. During our session heproved clear action items which I enjoyedcompleting. Each week we reviewed the progress and established new items to iteratetowards my goal. I am very thankful for my mentoring sessions with Evan.</p>
  <p class="quote-name">Jordan</p>
  <div class="carousel-arrow" style="left:201px">
    <svg width="12" height="12" viewBox="0 0 12 12"><path d="M8 1L3 6l5 5" fill="none" stroke="#fff" stroke-width="2.4" stroke-linecap="round" stroke-linejoin="round"/></svg>
  </div>
  <div class="carousel-arrow" style="left:956px">
    <svg width="12" height="12" viewBox="0 0 12 12"><path d="M4 1l5 5-5 5" fill="none" stroke="#fff" stroke-width="2.4" stroke-linecap="round" stroke-linejoin="round"/></svg>
  </div>
</section>

<footer class="site-footer">
  <div class="footer-dot"></div>
  <div class="footer-brand">GuideHarbor</div>
  <p class="footer-tag">Your trusted source to find highly - vetted mentors &amp; industry professionals to move your career a head.</p>
  <h3 class="footer-heading">Quick Licks</h3>
  <ul class="footer-list" style="left:568px;top:59px">
    <li>Browse Mentors</li><li>Became a Mentor</li><li>Partner Program</li><li>FAQ</li><li>Blog</li>
  </ul>
  <ul class="footer-list" style="left:904px;top:22px">
    <li>About Us</li><li>Code of Conduct</li><li>Privacy Policy</li><li>Success Stories</li><li>info@guideharbor.com</li>
  </ul>
  <span class="social-dot active" style="left:905px"></span>
  <span class="social-dot" style="left:942px"></span>
</footer>

</body>
</html>
```